Korvel Systems Business Cards
Elegant Business Cards
I need single sided standard sized Business Card [3.5" x 2"]
Futura
NONE
718 W. Alder Lane
Larkfield, Oregon 97031
info@korvelsystems-example.com
http://www.korvelsystems-example.com
I do not want to have a persons name on these cards since they will be generic and handed out in bulk.
Some or all of the following services
- Computer & Tablet Sales & Repair
- Business IT Services
- Networking
- Remote Support
- Virus & Spyware Removal
PNG of the logo - can be opened in fireworks and ALL Layers are present
Another version of logo in AI file, with all layers

```html
<!DOCTYPE html>
<html lang="en">
<head>
<meta charset="utf-8">
<title>Korvel Systems Stationery</title>
<link href="https://fonts.googleapis.com/css2?family=Jost:ital,wght@0,400;0,500;0,600;1,400&family=Open+Sans:wght@700&family=Arimo&display=swap" rel="stylesheet">
<style>
  :root{
    --board:#25272c;
    --navy:#1f3f63;
    --navy-light:#3d6290;
    --band-gray:#b9bcc0;
    --paper:#ffffff;
    --ink:#222222;
    --faint:#ececed;
    --label:#ffffff;
  }
  *{margin:0;padding:0;box-sizing:border-box}
  html,body{width:1200px;height:898px;overflow:hidden;background:var(--board)}
  body{position:relative;font-family:'Jost',sans-serif;color:var(--ink)}
  .option-label{position:absolute;font-family:'Open Sans',sans-serif;font-weight:700;font-size:12px;color:var(--label);letter-spacing:.2px}
  .piece{position:absolute;background:var(--paper);overflow:hidden;box-shadow:0 2px 6px rgba(0,0,0,.5)}
  .letterhead{top:36px;width:360px;height:467px}
  .abs{position:absolute;white-space:nowrap}
  .brand{position:absolute;display:flex;align-items:center;gap:7px;color:var(--navy)}
  .brand-dot{border-radius:50%;background:var(--navy);flex:none}
  .brand-name{font-family:'Jost',sans-serif;font-weight:500;line-height:1;letter-spacing:1px;text-transform:uppercase}
  .brand-name span{display:block}
  .brand--lg .brand-dot{width:34px;height:34px}
  .brand--lg .brand-name{font-size:21px}
  .brand--md .brand-dot{width:28px;height:28px}
  .brand--md .brand-name{font-size:18px}
  .brand--sm .brand-name{font-size:16px}
  .brand--white{color:#fff}
  .contact{font-size:6px;color:#333}
  .contact--right{text-align:right}
  .phone-strong{font-weight:600;color:var(--navy);font-size:9.5px}
  .phone-band{font-weight:600;color:#fff;font-size:9.5px}
  .url-spaced{font-size:7px;letter-spacing:1.2px;color:#333}
  .icon{display:inline-block;vertical-align:-1px;margin-right:2px}
  .watermark{position:absolute;border-radius:50%;background:var(--faint)}
  .bands{position:absolute;left:0}
  .fill-navy{fill:var(--navy)}
  .fill-gray{fill:var(--band-gray)}
  .fax-title{font-family:'Arimo',sans-serif;font-size:20px;color:#111}
  .form-row{position:absolute;font-family:'Arimo',sans-serif;font-size:6.5px;border-bottom:.6px solid #333;height:9px}
  .check{position:absolute;font-family:'Arimo',sans-serif;font-size:6.5px;display:flex;align-items:center;gap:4px}
  .check i{display:block;width:6.5px;height:6.5px;background:#d6d6d6}
  .envelope{top:546px;width:404px;height:222px;background:transparent;box-shadow:none;overflow:visible}
  .envelope-body{position:absolute;left:0;top:46px;width:404px;height:176px;background:var(--paper);overflow:hidden;box-shadow:0 2px 6px rgba(0,0,0,.5)}
  .envelope-flap{position:absolute;left:0;top:0}
  .card{width:274px;height:156px;border-radius:11px}
  .card-back{background:radial-gradient(circle at 40% 70%,var(--navy-light),var(--navy) 70%);color:#fff}
  .services-title{font-style:italic;font-size:12px}
  .service{font-size:10.5px;display:flex;align-items:center;gap:4px}
</style>
</head>
<body>

<div class="option-label" style="left:31px;top:9px">OPTION 1</div>
<div class="option-label" style="left:411px;top:6px">OPTION 2</div>
<div class="option-label" style="left:803px;top:6px">OPTION 3</div>

<!-- Fax sheet -->
<section class="piece letterhead" style="left:28px">
  <div class="brand brand--lg" style="left:23px;top:28px">
    <div class="brand-dot"></div>
    <div class="brand-name"><span>Korvel</span><span>Systems</span></div>
  </div>
  <div class="abs contact contact--right" style="right:29px;top:20px;line-height:11.8px">
    <div class="phone-strong"><svg class="icon" width="8" height="8" viewBox="0 0 10 10"><circle cx="5" cy="5" r="4.4" fill="none" stroke="#1f3f63"/><path d="M3.3 2.6l1 1-.6.8c.4.8 1 1.4 1.8 1.8l.8-.6 1 1-.8.9C4.8 7.3 2.7 5.2 2.5 3.4z" fill="#1f3f63"/></svg>888-555-0142</div>
    <div><svg class="icon" width="6" height="5" viewBox="0 0 12 9"><rect x=".5" y=".5" width="11" height="8" fill="none" stroke="#555"/><path d="M.5.5l5.5 4.5 5.5-4.5" fill="none" stroke="#555"/></svg>info@korvelsystems-example.com</div>
    <div>http://www.korvelsystems-example.com</div>
    <div>718 W. Alder Lane, Larkfield, Oregon 97031</div>
  </div>
  <div class="abs fax-title" style="left:23px;top:103px">FAX</div>
  <div class="form-row" style="left:23px;top:159px;width:309px"><span>To :</span><span class="abs" style="left:167px">From :</span></div>
  <div class="form-row" style="left:23px;top:178px;width:309px"><span>Fax :</span><span class="abs" style="left:167px">Page:</span></div>
  <div class="form-row" style="left:23px;top:197px;width:309px"><span>Phone :</span><span class="abs" style="left:167px">Date:</span></div>
  <div class="form-row" style="left:23px;top:216px;width:309px"><span>Re :</span><span class="abs" style="left:167px">CC:</span></div>
  <div class="check" style="left:23px;top:258px"><i></i>Urgent</div>
  <div class="check" style="left:70px;top:258px"><i></i>For Review</div>
  <div class="check" style="left:130px;top:258px"><i></i>Please Comment</div>
  <div class="check" style="left:206px;top:258px"><i></i>Please Reply</div>
  <div class="check" style="left:272px;top:258px"><i></i>Please Recycle</div>
  <svg class="bands" style="top:437px" width="360" height="25" viewBox="0 0 360 25">
    <polygon class="fill-gray" points="146,8 360,8 360,23 136,23"/>
    <polygon class="fill-navy" points="0,2 169,2 158,15 0,15"/>
  </svg>
</section>

<!-- Letterhead option 2 -->
<section class="piece letterhead" style="left:412px">
  <div class="watermark" style="left:200px;top:225px;width:190px;height:190px"></div>
  <div class="brand brand--lg" style="left:100px;top:26px">
    <div class="brand-dot"></div>
    <div class="brand-name"><span>Korvel</span><span>Systems</span></div>
  </div>
  <div class="abs contact" style="left:26px;top:414px"><svg class="icon" width="7" height="6" viewBox="0 0 12 9"><rect x=".5" y=".5" width="11" height="8" fill="none" stroke="#555"/><path d="M.5.5l5.5 4.5 5.5-4.5" fill="none" stroke="#555"/></svg>info@korvelsystems-example.com</div>
  <div class="abs contact contact--right" style="right:31px;top:420px">718 W. Alder Lane, Larkfield, Oregon 97031</div>
  <svg class="bands" style="top:425px" width="360" height="30" viewBox="0 0 360 30">
    <polygon class="fill-gray" points="148,10 360,10 360,27 138,27"/>
    <polygon class="fill-navy" points="0,2 169,2 158,18 0,18"/>
  </svg>
  <div class="abs phone-band" style="left:26px;top:428px"><svg class="icon" width="8" height="8" viewBox="0 0 10 10"><circle cx="5" cy="5" r="4.4" fill="none" stroke="#fff"/><path d="M3.3 2.6l1 1-.6.8c.4.8 1 1.4 1.8 1.8l.8-.6 1 1-.8.9C4.8 7.3 2.7 5.2 2.5 3.4z" fill="#fff"/></svg>888-555-0142</div>
  <div class="abs url-spaced" style="right:29px;top:437px">http://www.korvelsystems-example.com</div>
</section>

<!-- Letterhead option 3 -->
<section class="piece letterhead" style="left:805px">
  <div class="watermark" style="left:175px;top:215px;width:200px;height:200px"></div>
  <div class="brand brand--lg" style="left:25px;top:26px">
    <div class="brand-dot"></div>
    <div class="brand-name"><span>Korvel</span><span>Systems</span></div>
  </div>
  <div class="abs contact contact--right" style="right:24px;top:412px;line-height:10px">
    <div><svg class="icon" width="7" height="6" viewBox="0 0 12 9"><rect x=".5" y=".5" width="11" height="8" fill="none" stroke="#555"/><path d="M.5.5l5.5 4.5 5.5-4.5" fill="none" stroke="#555"/></svg>info@korvelsystems-example.com</div>
    <div>718 W. Alder Lane, Larkfield, Oregon 97031</div>
  </div>
  <svg class="bands" style="top:425px" width="360" height="30" viewBox="0 0 360 30">
    <polygon class="fill-gray" points="148,10 360,10 360,27 138,27"/>
    <polygon class="fill-navy" points="0,2 169,2 158,18 0,18"/>
  </svg>
  <div class="abs phone-band" style="left:26px;top:428px"><svg class="icon" width="8" height="8" viewBox="0 0 10 10"><circle cx="5" cy="5" r="4.4" fill="none" stroke="#fff"/><path d="M3.3 2.6l1 1-.6.8c.4.8 1 1.4 1.8 1.8l.8-.6 1 1-.8.9C4.8 7.3 2.7 5.2 2.5 3.4z" fill="#fff"/></svg>888-555-0142</div>
  <div class="abs url-spaced" style="right:24px;top:437px">http://www.korvelsystems-example.com</div>
</section>

<!-- Envelope option 1 -->
<section class="piece envelope" style="left:31px">
  <svg class="envelope-flap" width="404" height="47" viewBox="0 0 404 47">
    <path class="fill-navy" d="M0 47 L22 12 Q30 0 48 0 L356 0 Q374 0 382 12 L404 47 Z"/>
    <circle cx="201" cy="23" r="8" fill="#fff"/>
  </svg>
  <div class="envelope-body">
    <div class="watermark" style="left:275px;top:55px;width:150px;height:150px"></div>
    <div class="brand brand--md" style="left:17px;top:15px">
      <div class="brand-dot"></div>
      <div class="brand-name"><span>Korvel</span><span>Systems</span></div>
    </div>
    <svg class="bands" style="top:135px" width="404" height="32" viewBox="0 0 404 32">
      <polygon class="fill-gray" points="167,11 404,11 404,30 155,30"/>
      <polygon class="fill-navy" points="0,2 189,2 177,20 0,20"/>
    </svg>
    <div class="abs url-spaced" style="left:17px;top:141px;color:#fff;font-size:6.5px">http://www.korvelsystems-example.com</div>
    <div class="abs url-spaced" style="right:20px;top:151px;font-size:6.5px;letter-spacing:.6px">718 W. Alder Lane, Larkfield, Oregon 97031</div>
  </div>
</section>

<!-- Envelope option 2 -->
<section class="piece envelope" style="left:470px">
  <svg class="envelope-flap" width="404" height="47" viewBox="0 0 404 47">
    <path d="M0 47 L22 12 Q30 0 48 0 L356 0 Q374 0 382 12 L404 47 Z" fill="#fff"/>
    <circle cx="201" cy="20" r="8" class="fill-navy"/>
  </svg>
  <div class="envelope-body">
    <div class="watermark" style="left:225px;top:10px;width:170px;height:170px"></div>
    <div class="brand brand--md" style="left:17px;top:15px">
      <div class="brand-dot"></div>
      <div class="brand-name"><span>Korvel</span><span>Systems</span></div>
    </div>
    <div class="abs contact" style="left:28px;top:65px;font-size:6.5px">718 W. Alder Lane, Larkfield, Oregon 97031</div>
    <svg class="bands" style="top:135px" width="404" height="32" viewBox="0 0 404 32">
      <polygon class="fill-gray" points="167,11 404,11 404,30 155,30"/>
      <polygon class="fill-navy" points="0,2 189,2 177,20 0,20"/>
    </svg>
    <div class="abs url-spaced" style="left:24px;top:141px;color:#fff;font-size:6.5px">http://www.korvelsystems-example.com</div>
  </div>
</section>

<div class="option-label" style="left:35px;top:779px">OPTION 1</div>
<div class="option-label" style="left:472px;top:779px">OPTION 2</div>

<!-- Business card front -->
<section class="piece card" style="left:890px;top:538px">
  <div class="brand brand--md" style="left:61px;top:22px">
    <div class="brand-dot"></div>
    <div class="brand-name"><span>Korvel</span><span>Systems</span></div>
  </div>
  <div class="abs contact" style="left:17px;top:99px;font-size:7px"><svg class="icon" width="7" height="6" viewBox="0 0 12 9"><rect x=".5" y=".5" width="11" height="8" fill="none" stroke="#555"/><path d="M.5.5l5.5 4.5 5.5-4.5" fill="none" stroke="#555"/></svg>info@korvelsystems-example.com</div>
  <div class="abs contact contact--right" style="right:14px;top:92px;font-size:7px;line-height:9px">718 W. Alder Lane<br>Larkfield, Oregon 97031</div>
  <svg class="bands" style="top:112px" width="274" height="32" viewBox="0 0 274 32">
    <polygon class="fill-gray" points="128,11 274,11 274,29 118,29"/>
    <polygon class="fill-navy" points="0,2 151,2 140,21 0,21"/>
  </svg>
  <div class="abs phone-band" style="left:22px;top:115px;font-size:12px"><svg class="icon" width="10" height="10" viewBox="0 0 10 10"><circle cx="5" cy="5" r="4.4" fill="none" stroke="#fff"/><path d="M3.3 2.6l1 1-.6.8c.4.8 1 1.4 1.8 1.8l.8-.6 1 1-.8.9C4.8 7.3 2.7 5.2 2.5 3.4z" fill="#fff"/></svg>888-555-0142</div>
  <div class="abs contact" style="right:14px;top:128px;font-size:7px">http://www.korvelsystems-example.com</div>
</section>

<!-- Business card back -->
<section class="piece card card-back" style="left:892px;top:711px">
  <div class="abs services-title" style="left:19px;top:18px">services</div>
  <ul style="list-style:none">
    <li class="abs service" style="left:12px;top:41px"><svg width="7" height="7" viewBox="0 0 8 8"><path d="M2 1l4 3-4 3" fill="none" stroke="#fff" stroke-width="1.2"/></svg>Computer &amp; Tablet Sales &amp; Repair</li>
    <li class="abs service" style="left:12px;top:61px"><svg width="7" height="7" viewBox="0 0 8 8"><path d="M2 1l4 3-4 3" fill="none" stroke="#fff" stroke-width="1.2"/></svg>Business IT Services</li>
    <li class="abs service" style="left:12px;top:80px"><svg width="7" height="7" viewBox="0 0 8 8"><path d="M2 1l4 3-4 3" fill="none" stroke="#fff" stroke-width="1.2"/></svg>Networking</li>
    <li class="abs service" style="left:12px;top:100px"><svg width="7" height="7" viewBox="0 0 8 8"><path d="M2 1l4 3-4 3" fill="none" stroke="#fff" stroke-width="1.2"/></svg>Remote Support</li>
    <li class="abs service" style="left:12px;top:119px"><svg width="7" height="7" viewBox="0 0 8 8"><path d="M2 1l4 3-4 3" fill="none" stroke="#fff" stroke-width="1.2"/></svg>Virus &amp; Spyware Removal</li>
  </ul>
  <div class="brand brand--sm brand--white" style="right:8px;top:88px">
    <div class="brand-name" style="text-align:right"><span>Korvel</span><span>Systems</span></div>
  </div>
</section>

</body>
</html>
```